Business Card

I would like a business card with a picture of my husband and I that is unique and professional.

Industry/Entity Type

Business

Font styles to use
Serif

```html
<!DOCTYPE html>
<html lang="en">
<head>
<meta charset="utf-8">
<title>Marlow Leadership Group – Business Card</title>
<link rel="stylesheet" href="https://fonts.googleapis.com/css2?family=Jost:wght@400;600&family=Cinzel:wght@500&display=swap">
<style>
  :root{
    --bg:#3a3a3a;
    --card:#0c0c0c;
    --card-soft:#1a1a1a;
    --gold:#d9a93a;
    --gold-light:#f3d27a;
    --gold-deep:#9c6f1c;
  }
  *{margin:0;padding:0;box-sizing:border-box}
  html,body{width:1200px;height:1023px;overflow:hidden;background:var(--bg)}
  .canvas{position:relative;width:1200px;height:1023px}
  .card{position:absolute;width:520px;height:297px;background:var(--card);border-radius:4px;overflow:hidden;box-shadow:0 18px 40px rgba(0,0,0,.55)}
  .card--front{left:60px;top:140px}
  .card--back{left:620px;top:586px;background:radial-gradient(ellipse at center,#1c1c1c 0%,var(--card) 75%)}
  .swoosh{position:absolute;inset:0;width:100%;height:100%}
  .portrait{position:absolute;left:300px;top:22px;width:150px;height:106px;border-radius:6px;
    background:linear-gradient(160deg,#6b5548 0%,#3d302a 55%,#1e1a18 100%)}
  .brand{position:absolute;display:flex;align-items:center;gap:8px;color:var(--gold);
    font-family:"Jost",sans-serif;font-weight:600}
  .brand__dot{width:14px;height:14px;border-radius:50%;background:var(--gold)}
  .card--front .brand{left:30px;top:170px;font-size:15px}
  .contact{position:absolute;left:30px;top:200px;color:var(--gold);font-family:"Jost",sans-serif;line-height:1.25}
  .contact__name{font-weight:600;font-size:22px;color:var(--gold-light)}
  .contact__role,.contact__line{font-size:13px;font-weight:400}
  .card--back .brand{left:0;right:0;top:92px;justify-content:center;font-size:34px}
  .card--back .brand__dot{width:22px;height:22px}
  .company{position:absolute;left:0;right:0;top:160px;text-align:center;font-family:"Cinzel",serif;
    font-weight:500;font-size:15px;letter-spacing:1px;color:var(--gold)}
  .rule{position:absolute;left:130px;right:130px;top:186px;height:1px;background:var(--gold)}
  .tagline{position:absolute;left:0;right:0;top:200px;text-align:center;font-family:"Jost",sans-serif;
    font-size:18px;color:var(--gold)}
</style>
</head>
<body>
<main class="canvas">
  <section class="card card--front">
    <svg class="swoosh" viewBox="0 0 520 297" aria-hidden="true">
      <defs>
        <linearGradient id="goldBand" x1="0" y1="1" x2="1" y2="0">
          <stop offset="0" stop-color="#9c6f1c"/>
          <stop offset=".5" stop-color="#f3d27a"/>
          <stop offset="1" stop-color="#b98a2c"/>
        </linearGradient>
      </defs>
      <path d="M300 297 C400 230 440 110 470 0 L520 0 L520 297 Z" fill="#1d1d1d"/>
      <path d="M285 297 C385 230 425 110 455 0 L467 0 C437 112 398 236 302 297 Z" fill="url(#goldBand)"/>
      <path d="M320 297 C420 230 470 110 500 0 L505 0 C476 112 428 236 328 297 Z" fill="url(#goldBand)" opacity=".8"/>
    </svg>
    <div class="portrait" role="img" aria-label="Portrait photo of the couple in business attire"></div>
    <div class="brand"><span class="brand__dot"></span>Marlow Leadership Group</div>
    <div class="contact">
      <div class="contact__name">Dana Marlow</div>
      <div class="contact__role">Professional Mentorship Strategist</div>
      <div class="contact__line">312-555-0148</div>
      <div class="contact__line">DanaMarlow@example.com</div>
    </div>
  </section>

  <section class="card card--back">
    <div class="brand"><span class="brand__dot"></span>Marlow</div>
    <div class="company">Marlow Leadership Group</div>
    <div class="rule"></div>
    <div class="tagline">Growing Your Vision And Wealth Into Legacy!</div>
  </section>
</main>
</body>
</html>
```